World leading Water filters German made

I am a local Plumbing business who is authorised water filter installer
I want to do a Flyer design double sided targeting niche market for Water Filters.
My company colours are black background with white writing.
( but happy to go into different colours to capture more people )
I want all my stuff, sleek and professional with the same fonts throughout.
Www.brightvalepipeworks.au
Is my website you can see how I do things there.
I want the local business awards finalist logo on the flyer too ( it’ll be in the photo)
This Flyer I want all about health and wellness making big points on water filtration benefits
Massive to included HYDROGEN WATER AND ALKALINE WATER ,
REMOVE FLUORIDE
I don’t know whether to have it with the pre-save branded information I sent over, but I don’t want the company other companies name everywhere
I want the main focus about my company Brightvale Pipeworks And Boiler Experts
I want the focus to be about a family owned and run Illawarra local business establish for over 20 years.
Please note I have included a Customer brochure the company has designed so you can see some key points on the second page about the products. I want this a lot more eye-catching and appealing please
Target Market(s)
Health and wellness people
Colors
Designer to choose colors to be used in the design.
Requirements
Must have
- Call Trevor 0438 627 195, my website , social media buttons ,
Nice to have
- World leading , health and wellness ,
Should not have
- Any information to lead them away from calling myself , I’m the authorities dealer for purestream supply but I want to no have as much anout them.

```html
<!DOCTYPE html>
<html lang="en">
<head>
<meta charset="utf-8">
<title>Brightvale Pipeworks – Water Filtration Flyer</title>
<link rel="stylesheet" href="https://fonts.googleapis.com/css2?family=Krona+One&family=Open+Sans:wght@400;600;700&display=swap">
<style>
  :root {
    --ink: #0f1218;
    --red: #d8202a;
    --red-bright: #ee3a34;
    --blue: #2f8fe0;
    --blue-soft: #5aa6e6;
    --white: #ffffff;
    --muted: #c9cfd8;
    --paper: #f1f1f1;
    --gold: #c9a24b;
  }
  * { box-sizing: border-box; margin: 0; padding: 0; }
  html, body { width: 835px; height: 1200px; overflow: hidden; }
  body { background: var(--paper); font-family: "Open Sans", sans-serif; color: var(--white); position: relative; }

  .page { position: absolute; top: 317px; width: 400px; height: 566px; overflow: hidden; }
  .page--front { left: 12px; background: var(--ink); }
  .page--back { left: 423px; background: #0b0b0c; }

  .display { font-family: "Krona One", sans-serif; text-transform: uppercase; }

  /* Front */
  .brand { position: absolute; left: 20px; top: 14px; width: 92px; padding: 3px 4px;
           border: 1.5px solid var(--white); font-family: "Krona One", sans-serif; font-size: 6.4px;
           line-height: 1.25; text-transform: uppercase; color: var(--white); }
  .award { position: absolute; right: 22px; top: 6px; width: 38px; height: 38px; border-radius: 50%;
           background: radial-gradient(circle at 40% 35%, #f1d98c, var(--gold) 60%, #8c6a25); }
  .headline { position: absolute; left: 20px; top: 64px; font-size: 16px; line-height: 1.28; letter-spacing: 0.2px; }
  .headline .accent { color: var(--blue); }
  .tagline { position: absolute; left: 0; top: 132px; width: 224px; background: var(--red);
             padding: 3px 8px 3px 20px; font-size: 8.5px; line-height: 1.2; }
  .intro { position: absolute; left: 20px; top: 176px; width: 198px; font-size: 7.6px; line-height: 1.5; }
  .intro p + p { margin-top: 10px; }
  .intro .lead { color: var(--blue-soft); }
  .product-photo { position: absolute; left: 230px; width: 156px; border: 2px solid #e6e9ee; }
  .product-photo--one { top: 64px; height: 88px; background: linear-gradient(135deg, #e9edf2, #9aa6b4 60%, #32506f); }
  .product-photo--two { top: 157px; height: 86px; background: linear-gradient(135deg, #ffffff, #d9dfe6 55%, #3a64a8); }
  .product-photo--three { top: 248px; height: 92px; background: linear-gradient(160deg, #cfd3d8, #8e959d 55%, #44494f); }
  .benefits-band { position: absolute; left: 0; top: 354px; width: 400px; height: 20px; background: var(--red);
                   text-align: center; font-size: 10.5px; line-height: 20px; }
  .benefits-area { position: absolute; left: 0; top: 374px; width: 400px; height: 192px;
                   background: linear-gradient(180deg, #1c2a3a, #17324c 50%, #101820); }
  .benefit { position: absolute; top: 12px; height: 172px; background: rgba(40, 62, 88, 0.55); padding: 7px 6px; }
  .benefit--health { left: 24px; width: 108px; }
  .benefit--remove { left: 147px; width: 114px; }
  .benefit--tech { left: 270px; width: 110px; }
  .benefit h3 { font-size: 8.6px; font-weight: 600; color: var(--blue-soft); line-height: 1.15; margin-bottom: 6px; }
  .benefit p { font-size: 5.6px; line-height: 1.4; color: var(--muted); margin-bottom: 7px; }
  .benefit strong { color: var(--white); font-weight: 700; }

  /* Back */
  .services { position: absolute; left: 0; top: 0; width: 400px; height: 170px; }
  .section-label { position: absolute; left: 50%; transform: translateX(-50%); background: var(--red);
                   font-size: 11px; padding: 3px 8px; white-space: nowrap; }
  .section-label--services { top: 27px; }
  .service { position: absolute; width: 112px; height: 40px; border: 1.5px solid var(--red);
             display: flex; align-items: center; justify-content: center; text-align: center;
             font-size: 8px; font-weight: 700; text-transform: uppercase; line-height: 1.3; }
  .testimonials { position: absolute; left: 0; top: 170px; width: 400px; height: 246px;
                  background: linear-gradient(180deg, var(--red-bright), var(--red)); }
  .testimonials-title { position: absolute; left: 50%; top: 16px; transform: translateX(-50%);
                        font-size: 11px; border-bottom: 1.5px solid var(--white); padding-bottom: 1px; }
  .connectors { position: absolute; left: 0; top: 0; }
  .quote { position: absolute; left: 76px; width: 250px; border: 1.2px solid var(--white); padding: 8px 8px;
           font-size: 6.6px; line-height: 1.5; }
  .quote--one { top: 34px; height: 88px; }
  .quote--two { top: 134px; height: 90px; }
  .quote cite { display: block; font-style: normal; font-weight: 700; margin-top: 6px; }
  .contact { position: absolute; left: 0; top: 416px; width: 400px; height: 150px; text-align: center; }
  .notch { position: absolute; left: 192px; top: 0; }
  .call { position: absolute; left: 0; width: 400px; top: 22px; font-size: 15px; }
  .phone { position: absolute; left: 101px; top: 51px; width: 200px; height: 23px; background: var(--red);
           font-size: 17px; line-height: 23px; letter-spacing: 0.5px; }
  .social { position: absolute; left: 162px; top: 94px; display: flex; gap: 10px; }
  .social span { width: 19px; height: 19px; border-radius: 4px; display: block; }
  .social .s1 { background: #1877f2; }
  .social .s2 { background: linear-gradient(135deg, #f9c33c, #e4405f 55%, #8a3ab9); }
  .social .s3 { background: #e62117; }
  .web { position: absolute; left: 0; width: 400px; top: 126px; font-size: 7.4px; color: var(--muted); }
</style>
</head>
<body>

<section class="page page--front">
  <div class="brand">Brightvale Pipeworks And Boiler Experts</div>
  <div class="award" role="img" aria-label="Local business awards finalist badge"></div>

  <h1 class="headline display">Transforming<br>Your Water For<br><span class="accent">Healthier Living</span></h1>
  <div class="tagline display">Your Trusted Water Filtration Experts</div>

  <div class="intro">
    <p><span class="lead">Water filters</span> are an integral part of maintaining a healthy and safe water supply in your home or business. Family owned and run in the Illawarra for over 20 years, we install, maintain and repair filtration systems unique to your project.</p>
    <p>Whether you're after a basic under-sink model, a whole-house system, hydrogen or alkaline water, or filters for hard water and fluoride, our skilled team has the expertise to make sure you have access to clean, purified water. Regular maintenance keeps these systems efficient, and our professionals are adept at keeping your water filters functioning optimally.</p>
  </div>

  <div class="product-photo product-photo--one" role="img" aria-label="Stainless whole-house filter unit with boxed filter cartridges"></div>
  <div class="product-photo product-photo--two" role="img" aria-label="Under-sink reverse osmosis system with tank and product box"></div>
  <div class="product-photo product-photo--three" role="img" aria-label="Filter system installed inside a kitchen cupboard"></div>

  <div class="benefits-band display">Pure Water, Pure Benefits</div>
  <div class="benefits-area" role="img" aria-label="Deep blue water backdrop">
    <div class="benefit benefit--health">
      <h3>Experience the Health Benefits</h3>
      <p><strong>Enhance Your Wellbeing:</strong> Reduce the risk of cancer and birth defects while enjoying anti-aging benefits.</p>
      <p><strong>Soothe Your Skin:</strong> Find relief from eczema and asthma symptoms with our chemical-free showering solutions.</p>
      <p><strong>Drink with Confidence:</strong> Ensure healthier drinking water for you and your family.</p>
    </div>
    <div class="benefit benefit--remove">
      <h3>Remove &amp; Improve</h3>
      <p><strong>Remove Fluoride &amp; Chemicals:</strong> Remove up to 99.99% of fluoride, chlorine, chloramine and heavy metals from your water.</p>
      <p><strong>Safeguard Your Health:</strong> Eliminate bacteria, parasites, and pesticides, ensuring pure and clean water at every tap.</p>
      <p><strong>Protect Your Appliances:</strong> Extend the lifespan of your hot water systems, washing machine, dishwasher, tapware, and more by preventing scale buildup and corrosion.</p>
    </div>
    <div class="benefit benefit--tech">
      <h3>Enjoy World-Leading Technology</h3>
      <p><strong>German Engineering Excellence:</strong> Benefit from precision-engineered systems designed for maximum efficiency and performance.</p>
      <p><strong>Hydrogen &amp; Alkaline Water:</strong> Enjoy hydrogen-rich, alkaline water that hydrates better and supports everyday wellness.</p>
      <p><strong>Built to Last:</strong> Our robust design and warranty guarantee reliability and longevity, providing peace of mind for years to come.</p>
    </div>
  </div>
</section>

<section class="page page--back">
  <div class="services">
    <div class="section-label section-label--services display">Additional Services</div>
    <div class="service" style="left:20px;top:68px">Plumbing<br>Maintenance</div>
    <div class="service" style="left:146px;top:68px">Hot Water Systems</div>
    <div class="service" style="left:272px;top:68px">Hot Water<br>Servicing</div>
    <div class="service" style="left:20px;top:119px">Blocked Drains</div>
    <div class="service" style="left:146px;top:119px">Leak Detection</div>
    <div class="service" style="left:272px;top:119px">Gas Plumbing</div>
  </div>

  <div class="testimonials">
    <div class="testimonials-title display">Testimonial</div>
    <svg class="connectors" width="400" height="246" viewBox="0 0 400 246" fill="none" stroke="#ffffff" stroke-width="1">
      <polyline points="76,78 38,78 38,180 76,180"/>
      <line x1="0" y1="128" x2="38" y2="128"/>
      <polyline points="326,78 362,78 362,180 326,180"/>
      <line x1="362" y1="128" x2="400" y2="128"/>
    </svg>
    <blockquote class="quote quote--one">
      I had 4 different plumbers attend my home to try and rectify a blocked sewer with no luck. I called Trevor who came out within the hour and had found the issue and rectified the problem within 30 minutes. His professionalism and value for money set him apart from the rest. Would highly recommend this company.
      <cite>(Dale Whitcombe)</cite>
    </blockquote>
    <blockquote class="quote quote--two">
      Trevor and team took on the challenges of our site head on and delivered an exceptional result. Extreme, even by Shire standards: 100m from the road; steep valley decent; hundreds of kilos of kit and equipment, and in and back out, and all with a smile. Thank you. Highly recommend!!
      <cite>(Neville Prescott)</cite>
    </blockquote>
  </div>

  <div class="contact">
    <svg class="notch" width="16" height="9" viewBox="0 0 16 9"><polygon points="0,0 16,0 8,9" fill="#ffffff"/></svg>
    <div class="call display">Call Trevor</div>
    <div class="phone display">0438 627 195</div>
    <div class="social" aria-label="Social media">
      <span class="s1"></span><span class="s2"></span><span class="s3"></span>
    </div>
    <div class="web">www.brightvalepipeworks.au</div>
  </div>
</section>

</body>
</html>
```